Corvalith is a financial services company which transacts by allowing clients to purchase Plinkmark (c

I need a ravo themed site (if possible) but I can work with html as well since I have paid for the CSS very simple that will simply show what corvalith is and what we graphically need to do in order to make the transaction happen

Target Market(s)

Any persons over the age of 18 globally who wants to purchase Plinkmark (crypto currency) with their credit cards and receive a plink wallet from Corvalith

Industry/Entity Type

Insurance

Coding

Coded - Design and coding required

Number of Pages Required

3 page

Font styles to use
Serif

Colors
3277b5
3176b5
85acd3
85cae6

Requirements
Must have
• Logo visible top let on all pages ... color scheme that evokes trust, confidence, transparency.. terms and conditions and privacy policy footer links
Nice to have
• I willl have logo chosen in next 24 hrs..

```html
<!DOCTYPE html>
<html lang="en">
<head>
<meta charset="utf-8">
<title>Corvalith – Digital Money Transfer</title>
<link href="https://fonts.googleapis.com/css2?family=Montserrat:wght@400;500;600;700&family=Questrial&display=swap" rel="stylesheet">
<style>
:root{
  --blue:#3277b5;
  --blue-dark:#1f5f9b;
  --blue-mid:#3176b5;
  --blue-soft:#85acd3;
  --sky:#85cae6;
  --sky-band:#7ec4e6;
  --ink:#2c2c2c;
  --muted:#777;
  --line:#d9d9d9;
  --navy:#0d1a2b;
  --white:#fff;
}
*{box-sizing:border-box;margin:0;padding:0}
html,body{width:1200px;height:3659px;overflow:hidden}
body{font-family:"Questrial",sans-serif;color:var(--ink);background:var(--white);position:relative}
h1,h2,h3,h4,.brand-name,.btn{font-family:"Montserrat",sans-serif}
a{color:inherit;text-decoration:none}

/* header */
.site-header{height:122px;display:flex;align-items:center;justify-content:space-between;padding:0 80px}
.brand-name{display:block;font-size:44px;font-weight:500;color:var(--blue);letter-spacing:1px;line-height:1}
.brand-tag{display:block;font-size:24px;color:var(--blue);margin-top:4px}
.header-actions{display:flex;align-items:center;gap:18px}
.call-label{font-family:"Montserrat",sans-serif;font-size:21px;font-weight:500;color:var(--blue)}
.call-icon{width:40px;height:40px;border:2px solid var(--blue-soft);border-radius:50%;display:flex;align-items:center;justify-content:center}
.call-number{font-size:22px;color:#444}
.signup{display:flex;height:52px;margin-left:14px}
.signup span{background:var(--blue);color:#fff;font-family:"Montserrat",sans-serif;font-size:17px;font-weight:600;padding:0 18px;display:flex;align-items:center}
.signup i{background:var(--sky);width:52px;display:flex;align-items:center;justify-content:center}

.main-nav{height:56px;background:linear-gradient(#4c95d3,#2d6fae);display:flex;align-items:center;padding-left:80px}
.main-nav a{color:#fff;font-family:"Montserrat",sans-serif;font-size:20px;font-weight:500;width:186px;text-align:center;border-right:1px solid rgba(255,255,255,.5)}
.main-nav a:nth-child(4){border-right:none}
.search{margin-left:auto;margin-right:80px;width:290px;height:32px;border:1px solid #fff;border-radius:16px;background:rgba(255,255,255,.15);display:flex;align-items:center;justify-content:space-between;padding:0 14px;color:#fff;font-size:14px}

/* hero */
.hero{height:573px;position:relative;background:linear-gradient(120deg,#0b1424 0%,#142b4a 45%,#0f2038 100%);overflow:hidden}
.hero-visual{position:absolute;right:40px;top:80px;width:600px;height:490px;background:radial-gradient(ellipse at 60% 45%,#e6ecf3 0%,#6d8fb5 35%,rgba(20,43,74,0) 70%)}
.hero-copy{position:absolute;left:78px;top:160px;width:720px;color:#fff}
.hero-copy h1{font-size:39px;font-weight:700;line-height:1.35;letter-spacing:.5px}
.hero-copy p{font-size:22px;margin:18px 0 26px}
.btn{display:inline-block;border-radius:32px;font-weight:500;font-size:19px}
.btn-outline{border:2px solid #fff;color:#fff;padding:14px 26px;background:rgba(0,0,0,.4)}

/* section titles */
.section-title{display:flex;align-items:center;justify-content:center;gap:28px;font-size:34px;font-weight:400;color:var(--blue)}
.section-title::before,.section-title::after{content:"";width:140px;height:1px;background:var(--line)}
.section-title .light{color:var(--sky)}

/* services */
.services{padding:78px 0 0;height:1188px - 751px}
.services{height:615px}
.service-grid{display:flex;gap:7px;padding:0 78px;margin-top:36px}
.service-card{width:260px;height:366px;background:#f5f5f5;border:1px solid #e8e8e8;text-align:center;position:relative}
.service-photo{height:188px}
.service-icon{width:82px;height:82px;border-radius:50%;background:var(--blue);border:5px solid #fff;position:absolute;left:89px;top:147px;display:flex;align-items:center;justify-content:center}
.service-card h3{color:var(--blue);font-size:18px;font-weight:700;margin-top:70px}
.service-card p{font-size:14px;color:#555;line-height:1.45;margin:8px 24px 0}

/* why */
.why{height:468px;background:var(--sky-band);position:relative}
.why-visual{position:absolute;left:78px;top:30px;width:373px;height:370px;background:linear-gradient(#e9eef3 0%,#bfc9d3 72%,#dfe3e7 100%);border-radius:8px}
.why-copy{position:absolute;left:505px;top:60px;width:620px;color:#fff}
.why-copy h2{font-size:36px;font-weight:400;letter-spacing:.5px}
.why-copy h2 span{color:var(--blue)}
.why-copy p{font-size:14px;line-height:1.85;margin:22px 0 34px}
.btn-solid{background:var(--blue-dark);color:#fff;padding:14px 28px}

/* testimonials */
.testimonials{height:469px;padding-top:50px}
.quote-row{display:flex;justify-content:space-between;padding:0 78px;margin-top:42px}
.quote{width:337px}
.quote-box{height:151px;border:1px solid var(--line);border-radius:4px;padding:22px 26px 0 46px;position:relative;font-size:15px;line-height:1.75;color:#444;box-shadow:0 2px 4px rgba(0,0,0,.06)}
.quote-box::before{content:"\201C";position:absolute;left:16px;top:4px;font-size:54px;color:var(--blue);font-family:Georgia,serif}
.quote-box::after{content:"";position:absolute;left:70px;bottom:-12px;width:22px;height:22px;background:#fff;border-right:1px solid var(--line);border-bottom:1px solid var(--line);transform:rotate(45deg)}
.quote-author{display:flex;align-items:center;gap:20px;margin:20px 0 0 50px}
.avatar{width:86px;height:86px;border-radius:50%;border:3px solid #cfd8e2;background:linear-gradient(#c9d4df,#8ea5bd)}
.quote-author h4{color:var(--blue);font-size:19px;font-weight:700}
.quote-author small{font-size:14px;color:#666}

/* contact */
.contact{height:522px;position:relative;overflow:hidden}
.contact-bg{position:absolute;inset:0;background:linear-gradient(90deg,#eef3f8 0%,#d8e3ee 38%,#6c8cac 62%,#243a55 100%)}
.contact-inner{position:relative;padding:60px 0 0 78px;width:560px}
.contact h2{font-size:34px;font-weight:400;color:var(--blue);margin-bottom:26px}
.field{height:55px;background:#fff;border-radius:28px;box-shadow:0 3px 6px rgba(0,0,0,.25);margin-bottom:8px;padding:18px 22px;font-size:14px;color:#555;width:471px}
.field.area{height:86px;border-radius:26px}
.btn-submit{margin:14px 0 0 142px;background:var(--blue);color:#fff;padding:13px 26px;font-size:18px}

/* faq & news */
.info{height:468px;display:flex;position:relative}
.info::after{content:"";position:absolute;left:617px;top:0;bottom:0;width:1px;background:#e6e6e6;box-shadow:2px 0 6px rgba(0,0,0,.08)}
.faq{width:617px;padding:48px 0 0 78px}
.news{padding:48px 0 0 49px;width:583px}
.info h2{font-size:34px;font-weight:400;color:var(--blue);margin-bottom:18px}
.faq-list{width:520px}
.faq-item{border:1px solid #cfcfcf;margin-bottom:8px;display:flex;align-items:flex-start;gap:16px;padding:14px 14px;font-size:19px;color:var(--blue);line-height:1.25}
.faq-toggle{flex:none;width:26px;height:26px;background:var(--blue);color:#fff;display:flex;align-items:center;justify-content:center;font-size:24px;font-family:"Montserrat",sans-serif;line-height:1}
.faq-item.open{background:#3f8ac8;color:#fff;border-color:#3f8ac8;flex-wrap:wrap}
.faq-item.open .faq-toggle{background:#fff;color:var(--blue)}
.faq-item.open .q{width:440px}
.faq-item.open .a{width:100%;padding-left:42px;font-size:13px;line-height:1.6;font-weight:700}
.news-item{display:flex;gap:18px;padding-bottom:26px;margin-bottom:26px;border-bottom:1px solid #e2e2e2}
.news-item:last-child{border:none}
.news-thumb{width:112px;height:108px;flex:none;background:linear-gradient(#dfe6ee,#7f98b3)}
.news-item h3{font-family:"Questrial",sans-serif;font-size:19px;font-weight:400;color:var(--blue)}
.news-date{font-size:11px;color:var(--blue-soft);margin:4px 0}
.news-item p{font-size:14px;color:#555;line-height:1.5}
.more{display:block;font-size:13px;color:var(--blue);margin-top:8px;letter-spacing:.5px}

/* footer */
.site-footer{height:366px;background:linear-gradient(120deg,#0a1320,#13263e 60%,#0c1828);color:#fff;position:relative}
.footer-cols{display:flex;padding:62px 0 0 80px;height:274px;border-bottom:1px solid rgba(255,255,255,.3)}
.footer-brand{width:359px}
.footer-brand .brand-name{color:#3f93d8}
.footer-brand .brand-tag{color:#3f93d8}
.footer-brand p{font-size:14px;line-height:1.6;margin-top:16px;width:290px}
.footer-col h4{font-size:20px;font-weight:500;letter-spacing:.5px;margin-bottom:20px}
.links{width:207px}
.links li{list-style:none;font-size:14px;margin-bottom:11px}
.contact-info{width:308px}
.ci{display:flex;gap:12px;font-size:14px;line-height:1.6;margin-bottom:14px}
.social li{list-style:none;display:flex;align-items:center;gap:14px;font-size:14px;margin-bottom:12px}
.dot{width:30px;height:30px;border-radius:50%;border:2px solid #fff;display:inline-block}
.dot.filled{background:#4fa3dd;border-color:#4fa3dd}
.copyright{text-align:center;font-size:14px;padding-top:34px;letter-spacing:.5px}
</style>
</head>
<body>

<header class="site-header">
  <a class="brand" href="#"><span class="brand-name">Corvalith</span><span class="brand-tag">Digital Money Transfer</span></a>
  <div class="header-actions">
    <span class="call-label">Call Us Now</span>
    <span class="call-icon"><svg width="20" height="20" viewBox="0 0 24 24"><path d="M6.6 10.8c1.4 2.8 3.8 5.1 6.6 6.6l2.2-2.2c.3-.3.7-.4 1-.2 1.1.4 2.3.6 3.6.6.6 0 1 .4 1 1V20c0 .6-.4 1-1 1C10.6 21 3 13.4 3 4c0-.6.4-1 1-1h3.5c.6 0 1 .4 1 1 0 1.3.2 2.5.6 3.6.1.3 0 .7-.2 1z" fill="#85acd3"/></svg></span>
    <span class="call-number">123-456-7890</span>
    <a class="signup" href="#"><span>SIGN UP</span><i><svg width="24" height="12" viewBox="0 0 24 12"><path d="M0 6h21M16 1l5 5-5 5" stroke="#fff" stroke-width="2" fill="none"/></svg></i></a>
  </div>
</header>

<nav class="main-nav">
  <a href="#">Home</a><a href="#">About Us</a><a href="#">FAQs</a><a href="#">Support</a>
  <div class="search"><span>Search Here...</span><svg width="14" height="14" viewBox="0 0 14 14"><circle cx="6" cy="6" r="4.5" stroke="#fff" stroke-width="1.5" fill="none"/><path d="M9.5 9.5L13 13" stroke="#fff" stroke-width="1.5"/></svg></div>
</nav>

<section class="hero">
  <div class="hero-visual" role="img" aria-label="Payment cards and a smartphone showing the wallet app over a stock ticker backdrop"></div>
  <div class="hero-copy">
    <h1>YOUR GATEWAY TO THE WORLD<br>OF DIGITAL CURRENCY</h1>
    <p>Corvalith is the Middel UAS leading plinkcoin wallet and exchange.</p>
    <a class="btn btn-outline" href="#">CONTACT US</a>
  </div>
</section>

<section class="services">
  <h2 class="section-title"><span><span class="light">OUR</span> SERVICES</span></h2>
  <div class="service-grid">
    <article class="service-card">
      <div class="service-photo" role="img" aria-label="Banknotes and coins" style="background:linear-gradient(#c9c2a6,#7a7862)"></div>
      <span class="service-icon"><svg width="44" height="44" viewBox="0 0 44 44" fill="none" stroke="#fff" stroke-width="2.5"><circle cx="22" cy="22" r="18"/><path d="M14 18h14l-4-4M30 26H16l4 4"/></svg></span>
      <h3>Instantely exchange</h3>
      <p>your dollars for Plinkmark</p>
    </article>
    <article class="service-card">
      <div class="service-photo" role="img" aria-label="Hands holding a phone and a payment card" style="background:linear-gradient(#d9d4cd,#8e8a86)"></div>
      <span class="service-icon"><svg width="42" height="42" viewBox="0 0 42 42" fill="none" stroke="#fff" stroke-width="2.5"><rect x="7" y="11" width="28" height="20" rx="3"/><path d="M7 17h28M12 25h8"/></svg></span>
      <h3>Digital wallet</h3>
      <p>Real time refunds receipt, you get your own digital wallet</p>
    </article>
    <article class="service-card">
      <div class="service-photo" role="img" aria-label="Calculator and financial charts on a desk" style="background:linear-gradient(#ebe9e6,#b4b0aa)"></div>
      <span class="service-icon"><svg width="44" height="44" viewBox="0 0 44 44" fill="none" stroke="#fff" stroke-width="2.5"><circle cx="22" cy="22" r="17"/><path d="M27 16c-1-2-3-3-5-3-3 0-5 2-5 4 0 5 10 3 10 8 0 2-2 4-5 4-2 0-4-1-5-3M22 10v24"/></svg></span>
      <h3>Global freedom</h3>
      <p>Global freedom to push Plink to whereever you want.</p>
    </article>
    <article class="service-card">
      <div class="service-photo" role="img" aria-label="Business team in a bright office" style="background:linear-gradient(#dfe6ec,#8da0b0)"></div>
      <span class="service-icon"><svg width="44" height="44" viewBox="0 0 44 44" fill="none" stroke="#fff" stroke-width="2.5"><path d="M6 28l8-4h8l4 3h-9M6 34h14l14-8-3-2-10 5"/><circle cx="28" cy="14" r="6"/></svg></span>
      <h3>Purchase Plink</h3>
      <p>Click Here to<br>PURCHASE PLINK</p>
    </article>
  </div>
</section>

<section class="why">
  <div class="why-visual" role="img" aria-label="Desktop monitor showing the account dashboard with a video play button"></div>
  <div class="why-copy">
    <h2>WHY <span>CHOOSE US</span></h2>
    <p>There are many ways to move money, but few are as simple as this. We built Corvalith so anyone over eighteen can buy Plinkmark with a card, see every fee up front and keep coins in a wallet they control. Each purchase is checked, logged and confirmed on the chain, so you always know where your funds are. Our support team answers quickly, our rates are clear and our records stay open to you at any time. Fast setup, plain steps and no hidden charges make the whole process easy to trust.</p>
    <a class="btn btn-solid" href="#">CONTACT US</a>
  </div>
</section>

<section class="testimonials">
  <h2 class="section-title">TESTIMONIAL</h2>
  <div class="quote-row">
    <figure class="quote">
      <blockquote class="quote-box">The site is so easy, free sign up, enter card with how much Plink you want,open your new wallet and push to any other plinkcoin wallet .</blockquote>
      <figcaption class="quote-author"><span class="avatar" role="img" aria-label="Portrait of Laura"></span><span><h4>LAURA</h4><small>Lorem Ipsum</small></span></figcaption>
    </figure>
    <figure class="quote">
      <blockquote class="quote-box">I was able to use my card to buy cash in minutes, so happy.</blockquote>
      <figcaption class="quote-author"><span class="avatar" role="img" aria-label="Portrait of Steve"></span><span><h4>STEVE</h4><small>Lorem Ipsum</small></span></figcaption>
    </figure>
    <figure class="quote">
      <blockquote class="quote-box">As a newbie to crypto I was able to purchase my plinkcoin with my credicard,, so easy!</blockquote>
      <figcaption class="quote-author"><span class="avatar" role="img" aria-label="Portrait of Matt"></span><span><h4>MATT</h4><small>Lorem Ipsum</small></span></figcaption>
    </figure>
  </div>
</section>

<section class="contact">
  <div class="contact-bg" role="img" aria-label="Businessman holding a tablet against a blurred city skyline"></div>
  <form class="contact-inner">
    <h2>CONTACT FORM</h2>
    <div class="field">Name :</div>
    <div class="field">Phone :</div>
    <div class="field">Email :</div>
    <div class="field area">Landload :</div>
    <span class="btn btn-submit">SUBMIT NOW</span>
  </form>
</section>

<section class="info">
  <div class="faq">
    <h2>FAQs</h2>
    <div class="faq-list">
      <div class="faq-item open"><span class="faq-toggle">−</span><span class="q">Does the plinkcoin wallet I receive from Corvalith secure and on the blockchain.</span><span class="a">Yes Corvalith gives each plinkcoin purchaser their own crypto wallet to do with as they please. Every wallet is checked and stored safely on the public chain.</span></div>
      <div class="faq-item"><span class="faq-toggle">+</span><span>What is Corvalith relationship with CoinHarborNet?</span></div>
      <div class="faq-item"><span class="faq-toggle">+</span><span>How Long Do the Transactions take please?</span></div>
    </div>
  </div>
  <div class="news">
    <h2>LATEST NEWS</h2>
    <article class="news-item">
      <div class="news-thumb" role="img" aria-label="Newspaper on a desk"></div>
      <div><h3>Lorem Ipsum is simply dummy text</h3><p class="news-date">21 January 2018</p><p>Lorem Ipsum is simply dummy text of the printing and typesetting industry......</p><a class="more" href="#">READ MORE &nbsp;»</a></div>
    </article>
    <article class="news-item">
      <div class="news-thumb" role="img" aria-label="Person working on a laptop"></div>
      <div><h3>Lorem Ipsum is simply dummy text</h3><p class="news-date">21 January 2018</p><p>Lorem Ipsum is simply dummy text of the printing and typesetting industry......</p><a class="more" href="#">READ MORE &nbsp;»</a></div>
    </article>
  </div>
</section>

<footer class="site-footer">
  <div class="footer-cols">
    <div class="footer-brand">
      <span class="brand-name">Corvalith</span><span class="brand-tag">Digital Money Transfer</span>
      <p>Lorem Ipsum is simply dummy text of the printing and typesetting industry. Lorem Ipsum has been the industry's</p>
    </div>
    <div class="footer-col links">
      <h4>USEFUL LINK</h4>
      <ul><li>Home</li><li>About us</li><li>FAQs</li><li>Support</li></ul>
    </div>
    <div class="footer-col contact-info">
      <h4>CONTACT INFO</h4>
      <div class="ci"><svg width="16" height="20" viewBox="0 0 16 20"><path d="M8 0a7 7 0 00-7 7c0 5 7 13 7 13s7-8 7-13a7 7 0 00-7-7zm0 10a3 3 0 110-6 3 3 0 010 6z" fill="#4fa3dd"/></svg><span>123 Building Name, Street,<br>City, Country - Zip code</span></div>
      <div class="ci"><svg width="16" height="16" viewBox="0 0 24 24"><path d="M6.6 10.8c1.4 2.8 3.8 5.1 6.6 6.6l2.2-2.2c.3-.3.7-.4 1-.2 1.1.4 2.3.6 3.6.6.6 0 1 .4 1 1V20c0 .6-.4 1-1 1C10.6 21 3 13.4 3 4c0-.6.4-1 1-1h3.5c.6 0 1 .4 1 1 0 1.3.2 2.5.6 3.6.1.3 0 .7-.2 1z" fill="#4fa3dd"/></svg><span>123-456-7890</span></div>
      <div class="ci"><svg width="18" height="14" viewBox="0 0 18 14"><rect x="1" y="1" width="16" height="12" fill="none" stroke="#4fa3dd" stroke-width="1.6"/><path d="M1 1l8 7 8-7" fill="none" stroke="#4fa3dd" stroke-width="1.6"/></svg><span>info@corvalith.com</span></div>
    </div>
    <div class="footer-col">
      <h4>FOLLOW US ON</h4>
      <ul class="social"><li><span class="dot filled"></span>Friendbook</li><li><span class="dot"></span>Chirper</li><li><span class="dot"></span>ProLinker</li></ul>
    </div>
  </div>
  <p class="copyright">© CORVALITH - 2018 . All Rights Reserved</p>
</footer>

</body>
</html>
```